Accounting business needs business card

I have a business card but need something better. I want the colour changed and the design to be better. I have uploaded a picture of my new sign that is grey in colour, i would like to incorporate these colours.

```html
<!DOCTYPE html>
<html lang="en">
<head>
<meta charset="utf-8">
<title>Nilbrook Tax Business Card</title>
<link rel="stylesheet" href="https://fonts.googleapis.com/css2?family=Montserrat:wght@400;500;600;700&display=swap">
<style>
  :root {
    --page-bg: #3b3b3d;
    --card-white: #fbfbfb;
    --card-grey-light: #ececec;
    --card-grey-mid: #dedede;
    --ink: #232427;
    --accent-blue: #12b2ea;
    --accent-blue-light: #2ec3f2;
    --watermark: #e6e6e6;
    --badge-navy: #1b4c8c;
    --badge-gold: #f2c200;
    --badge-green: #8cc63f;
    --badge-grey: #d4d4d4;
    --divider: #a9a9a9;
  }
  * { box-sizing: border-box; margin: 0; padding: 0; }
  html, body { width: 1200px; height: 900px; overflow: hidden; }
  body {
    background: var(--page-bg);
    font-family: "Montserrat", Arial, sans-serif;
    color: var(--ink);
    position: relative;
  }
  .card {
    position: absolute;
    left: 250px;
    width: 700px;
    height: 400px;
    overflow: hidden;
    box-shadow: 0 10px 28px rgba(0,0,0,0.45);
  }

  /* Contact side */
  .card-contact { top: 36px; background: var(--card-white); }
  .watermark-ring {
    position: absolute;
    right: 70px; top: -120px;
    width: 330px; height: 330px;
    border: 5px solid var(--watermark);
    border-radius: 50%;
  }
  .brand-small { position: absolute; left: 48px; top: 44px; display: flex; flex-direction: column; align-items: center; }
  .brand-small .brand-dot {
    width: 76px; height: 76px;
    border: 3px solid var(--ink);
    border-radius: 50%;
  }
  .brand-small .brand-name {
    margin-top: 16px;
    font-weight: 600;
    font-size: 22px;
    letter-spacing: 11px;
    color: var(--ink);
  }
  .person { position: absolute; left: 52px; top: 176px; }
  .person-name {
    font-weight: 700;
    font-size: 24px;
    letter-spacing: 1px;
    color: var(--accent-blue);
  }
  .person-role { font-size: 15px; font-weight: 500; line-height: 1.3; margin-top: 4px; }
  .contact-list { position: absolute; left: 52px; top: 276px; list-style: none; }
  .contact-list li {
    display: flex; align-items: center;
    font-size: 16px; font-weight: 500;
    height: 30px;
  }
  .contact-icon { width: 24px; height: 24px; margin-right: 14px; flex: none; }
  .badges {
    position: absolute; right: 36px; bottom: 38px;
    display: flex; align-items: center; gap: 14px;
  }
  .badge-block { display: flex; flex-direction: column; align-items: center; gap: 6px; }
  .badge-bar { display: flex; width: 110px; height: 26px; }
  .badge-bar .navy { flex: 1; background: var(--badge-navy); }
  .badge-bar .gold { width: 40px; background: var(--badge-gold); }
  .badge-seal {
    width: 54px; height: 54px; border-radius: 50%;
    border: 4px solid var(--badge-grey);
    background: var(--card-white);
    display: flex; align-items: center; justify-content: center;
  }
  .badge-seal span { width: 24px; height: 24px; border-radius: 50%; background: var(--badge-green); }
  .badge-round { width: 52px; height: 52px; border-radius: 50%; background: var(--accent-blue); }
  .badge-caption { font-size: 8px; line-height: 1.2; text-align: center; color: var(--ink); }
  .badge-divider { width: 2px; height: 38px; background: var(--divider); }

  /* Front side */
  .card-front {
    top: 464px;
    background: linear-gradient(100deg, var(--card-grey-light) 0%, var(--card-grey-mid) 55%, var(--card-grey-light) 100%);
  }
  .brand-large { position: absolute; left: 0; right: 0; top: 46px; display: flex; flex-direction: column; align-items: center; }
  .brand-large .brand-dot {
    width: 150px; height: 150px;
    border: 4px solid var(--ink);
    border-radius: 50%;
  }
  .brand-large .brand-name {
    margin-top: 28px;
    font-weight: 600;
    font-size: 40px;
    letter-spacing: 20px;
    padding-left: 20px;
    color: var(--ink);
  }
  .web-band {
    position: absolute; left: 0; right: 0; top: 292px; height: 52px;
    background: linear-gradient(90deg, var(--accent-blue) 0%, var(--accent-blue-light) 50%, var(--accent-blue) 100%);
    display: flex; align-items: center; justify-content: center;
  }
  .web-band span { font-weight: 700; font-size: 30px; color: var(--ink); }
</style>
</head>
<body>

<section class="card card-contact">
  <div class="watermark-ring"></div>

  <div class="brand-small">
    <div class="brand-dot"></div>
    <div class="brand-name">NILBROOK TAX</div>
  </div>

  <div class="person">
    <div class="person-name">OWEN HARTLEY</div>
    <div class="person-role">CPA, MTAX, B.COM (Acc &amp; Fin)<br>Taxation and Business Account</div>
  </div>

  <ul class="contact-list">
    <li>
      <svg class="contact-icon" viewBox="0 0 24 24" aria-hidden="true">
        <circle cx="12" cy="12" r="10.5" fill="none" stroke="var(--accent-blue)" stroke-width="2"/>
        <path d="M8.5 7.5l2 .3.8 2.3-1.3 1a6 6 0 0 0 3 3l1-1.3 2.3.8.3 2a1.3 1.3 0 0 1-1.4 1.2A8.5 8.5 0 0 1 7.3 8.9 1.3 1.3 0 0 1 8.5 7.5z" fill="var(--accent-blue)"/>
      </svg>
      0400 555 018
    </li>
    <li>
      <svg class="contact-icon" viewBox="0 0 24 24" aria-hidden="true">
        <circle cx="12" cy="12" r="10.5" fill="none" stroke="var(--accent-blue)" stroke-width="2"/>
        <circle cx="12" cy="12" r="6" fill="none" stroke="var(--accent-blue)" stroke-width="1.4"/>
        <ellipse cx="12" cy="12" rx="2.6" ry="6" fill="none" stroke="var(--accent-blue)" stroke-width="1.2"/>
        <path d="M6 12h12M7 9h10M7 15h10" stroke="var(--accent-blue)" stroke-width="1.1"/>
      </svg>
      www.nilbrooktax.com.au
    </li>
    <li>
      <svg class="contact-icon" viewBox="0 0 24 24" aria-hidden="true">
        <circle cx="12" cy="12" r="10.5" fill="none" stroke="var(--accent-blue)" stroke-width="2"/>
        <rect x="6.5" y="8" width="11" height="8" rx="1" fill="var(--accent-blue)"/>
        <path d="M6.8 8.4l5.2 4 5.2-4" fill="none" stroke="var(--card-white)" stroke-width="1.1"/>
      </svg>
      owen@nilbrooktax.com.au
    </li>
  </ul>

  <div class="badges">
    <div class="badge-block">
      <div class="badge-bar"><span class="navy"></span><span class="gold"></span></div>
      <div class="badge-caption">Member practice</div>
    </div>
    <div class="badge-divider"></div>
    <div class="badge-block">
      <div class="badge-seal"><span></span></div>
      <div class="badge-caption">Tax agent<br>10203040</div>
    </div>
    <div class="badge-divider"></div>
    <div class="badge-round"></div>
  </div>
</section>

<section class="card card-front">
  <div class="brand-large">
    <div class="brand-dot"></div>
    <div class="brand-name">NILBROOK TAX</div>
  </div>
  <div class="web-band"><span>www.nilbrooktax.com.au</span></div>
</section>

</body>
</html>
```